ultra-minimalist business card

front (black background, matte):

tarik b. hosseny
writer | photographer
get@tarikhosseny.com

back (white background, matte):

a picture speaks a thousand words;
a word draws a thousand pictures.

www.tarikhosseny.com

all text should be small (white or silver - as long as it shows against the black - on the front; black or gray - as long as it shows against the white - on the back).

feel free to get creative in terms of arrangement, alignment, and font type, but remember, the overall style is minimalist, so nothing too fancy, please.

thanks.

```html
<!DOCTYPE html>
<html lang="en">
<head>
<meta charset="utf-8">
<title>Tarik B. Hosseny — Business Card</title>
<link rel="stylesheet" href="https://fonts.googleapis.com/css2?family=Courier+Prime:wght@400;700&family=Montserrat:wght@700&display=swap">
<style>
  :root {
    --page: #ffffff;
    --ink: #1a1a1a;
    --card-dark: #000000;
    --card-light: #ffffff;
    --paper-text: #ffffff;
    --shadow: rgba(0, 0, 0, 0.35);
  }
  html, body {
    margin: 0;
    padding: 0;
    width: 1200px;
    height: 1200px;
    overflow: hidden;
    background: var(--page);
  }
  .sheet {
    position: relative;
    width: 1200px;
    height: 1200px;
  }
  .version-label {
    position: absolute;
    left: 96px;
    top: 596px;
    transform: translate(-50%, -50%) rotate(-90deg);
    font-family: "Montserrat", sans-serif;
    font-weight: 700;
    font-size: 40px;
    letter-spacing: -0.5px;
    color: var(--ink);
    white-space: nowrap;
    margin: 0;
  }
  .card {
    position: absolute;
    box-shadow: 0 4px 6px var(--shadow);
  }
  .card svg { display: block; }
  .card--front {
    left: 188px;
    top: 44px;
    width: 824px;
    height: 532px;
    background: var(--card-dark);
  }
  .card--back {
    left: 190px;
    top: 620px;
    width: 820px;
    height: 532px;
    background: var(--card-light);
  }
  .typewriter {
    font-family: "Courier Prime", monospace;
  }
  .front-text { fill: var(--paper-text); font-size: 36px; letter-spacing: -1px; }
  .first-name { fill: var(--paper-text); font-size: 34px; letter-spacing: -1px; }
  .quote-text { fill: var(--ink); font-size: 31px; }
  .quote-text .key { font-weight: 700; }
  .quote-mark { fill: var(--ink); }
  .site-url { fill: var(--ink); font-size: 32px; font-weight: 700; letter-spacing: -1px; }
</style>
</head>
<body>
<main class="sheet">
  <p class="version-label">VERSION 01</p>

  <section class="card card--front" aria-label="Card front">
    <svg width="824" height="532" viewBox="0 0 824 532" class="typewriter">
      <text class="first-name" x="720" y="162" text-anchor="end">tarik</text>
      <g class="contact">
        <text class="front-text" x="52" y="362">tarik b. hosseny</text>
        <text class="front-text" x="52" y="414">writer | photographer</text>
        <text class="front-text" x="52" y="465">get@tarikhosseny.com</text>
      </g>
    </svg>
  </section>

  <section class="card card--back" aria-label="Card back">
    <svg width="820" height="532" viewBox="0 0 820 532" class="typewriter">
      <g class="quote-open" transform="translate(158 96)">
        <path class="quote-mark" d="M2,26 C2,12 10,3 22,0 L23,3 C15,8 11,14 13,19 A11,11 0 1 1 2,26 Z"/>
        <path class="quote-mark" transform="translate(30 0)" d="M2,26 C2,12 10,3 22,0 L23,3 C15,8 11,14 13,19 A11,11 0 1 1 2,26 Z"/>
      </g>
      <g class="quote-text" text-anchor="middle">
        <text x="414" y="136">a <tspan class="key">picture</tspan> speaks a</text>
        <text x="414" y="180">thousand words;</text>
        <text x="412" y="270">a <tspan class="key">word</tspan> draws a</text>
        <text x="412" y="314">thousand pictures.</text>
      </g>
      <g class="quote-close" transform="translate(672 332) rotate(180)">
        <path class="quote-mark" d="M2,26 C2,12 10,3 22,0 L23,3 C15,8 11,14 13,19 A11,11 0 1 1 2,26 Z"/>
        <path class="quote-mark" transform="translate(30 0)" d="M2,26 C2,12 10,3 22,0 L23,3 C15,8 11,14 13,19 A11,11 0 1 1 2,26 Z"/>
      </g>
      <text class="site-url" x="410" y="448" text-anchor="middle">www.tarikhosseny.com</text>
    </svg>
  </section>
</main>
</body>
</html>
```